Website Landing Page for Brightfall Systems

Create a custom designed website landing page for our business. Looking for a professional upscale design that incorporates our logo and logo colors into the theme. I want a standard fixed frame website, not a constant scrolling format that seems to be the trend. To start with I'm looking for more of the graphic design part, maybe a concept or theme, I don't expect to see a finished project. Not interested in generic templates or layouts.

The name of our company is Brightfall Systems and I've attached our logo below. I'd like to have the web page have the same look and feel of our logo, as well as the colors. Our company, Brightfall Systems does system design, installation, and programming, of residential and commercial Audio/Video and Automation systems. We do home theaters, lighting and building automation, video conferencing systems, security camera installations, conference rooms, projectors, distributed audio systems, and similar Technology projects. This will be a professional services/informational website. We will not sell products on this website. This website will be used to advertise our company and communicate our services to prospective customers. Having a well designed, professional and clean website is one way we want to distinguish our company from the competition.

Here are some examples of what I consider a professional well designed website
http://www.qorlamstudio.com/Work/

Last year we had our tradlo store designed (with PixelMarket) and I'm really happy with the way it turned out. You can see it at www.HolvenGearDepot.com I consider this to be a great design and looking for the same level of quality with this new website. However, do not copy or use any part of this design in this new project. This tradlo store is completely separate from our other company Brightfall Systems. I only mention this tradlo store an an example of good work.

Reason: Still going through designs.

Reason: Still working on project and have not had time to review all designs and request revisions.

Reason: Sill going through designs and requesting revisions

Reason: still going through all the submissions we received.

Target Market(s)

People interested in Audio/Video, home theaters, home automation. We do sales, system design, and programming. We typically work on larger projects with both residential and commercial customers.

Industry/Entity Type

Business

Number of Pages Required

1 page

Requirements
Must have
• Great design elements. Please use a white background. I think white goes well with our logo colors.

```html
<!DOCTYPE html>
<html lang="en">
<head>
<meta charset="utf-8">
<title>Brightfall Systems</title>
<link href="https://fonts.googleapis.com/css2?family=Source+Sans+3:wght@400;600;700&display=swap" rel="stylesheet">
<style>
:root{
  --green:#6dbb45;
  --green-dark:#4f9a2c;
  --blue:#2f7fc8;
  --navy:#1f4f7a;
  --ink:#333;
  --muted:#777;
  --line:#ddd;
  --grey:#f1f1f1;
}
*{box-sizing:border-box;margin:0;padding:0}
html,body{width:1200px;height:2216px;overflow:hidden}
body{font-family:"Source Sans 3",Arial,sans-serif;color:var(--ink);background:#fff;position:relative}
.site-header{height:50px;display:flex;align-items:center;justify-content:space-between;padding:0 240px}
.brand{display:flex;align-items:center;gap:8px;color:var(--blue);font-weight:700;font-size:17px;letter-spacing:.5px;text-transform:uppercase}
.brand-dot{width:26px;height:26px;border-radius:50%;background:var(--green)}
.main-nav{display:flex;gap:16px;font-size:11px;color:var(--muted)}
.main-nav a{color:inherit;text-decoration:none;padding-bottom:3px}
.main-nav a.active{color:var(--green);border-bottom:2px solid var(--green)}

.hero{height:370px;position:relative}
.hero-photo{position:absolute;inset:0;background:linear-gradient(180deg,#3a3f45 0%,#6b6f74 45%,#2b2e31 100%)}
.hero-box{position:absolute;left:240px;top:20px;width:720px;height:270px;background:rgba(255,255,255,.72)}
.hero-title{font-size:32px;color:var(--navy);font-weight:600;padding:14px 0 6px 14px}
.hero-tag{background:var(--green);color:#fff;font-size:20px;padding:6px 14px;width:560px}
.hero-text{font-size:13px;line-height:1.4;color:#222;padding:10px 14px;width:560px}
.hero-btn{position:absolute;left:500px;top:300px;width:200px;height:40px;background:var(--green);color:#fff;font-size:16px;display:flex;align-items:center;justify-content:center;border:2px solid #fff}
.hero-arrow{position:absolute;top:160px;width:30px;height:30px;border-radius:50%;background:rgba(255,255,255,.85);display:flex;align-items:center;justify-content:center}
.hero-arrow.prev{left:170px}.hero-arrow.next{right:170px}

.actions{height:220px;background:var(--blue);display:flex;justify-content:center;gap:50px;padding-top:42px}
.action{width:200px;text-align:center;color:#fff}
.action svg{display:block;margin:0 auto 6px}
.action h3{font-size:26px;font-weight:400;line-height:1;white-space:nowrap}
.action p{font-size:11px;margin:4px 0 10px;opacity:.9}
.btn-go{display:inline-block;background:var(--green);color:#fff;font-size:11px;padding:3px 18px}

.welcome{height:300px;text-align:center;padding-top:52px}
.welcome h1{font-size:36px;font-weight:400;color:#222}
.welcome p{width:560px;margin:14px auto 16px;font-size:12px;line-height:1.45;color:#555}
.btn-outline{display:inline-block;border:1px solid #bbb;font-size:11px;padding:3px 14px;color:#555}

.why{height:470px}
.why h2{text-align:center;font-size:21px;font-weight:400;color:#444;padding-top:30px;margin-bottom:14px}
.why-grid{width:712px;margin:0 auto;display:grid;grid-template-columns:1fr 1fr;gap:4px}
.tile{height:190px;position:relative}
.tile .photo{position:absolute;inset:0}
.tile-cap{position:absolute;bottom:0;left:0;right:0;background:rgba(0,0,0,.55);color:#fff;padding:4px 8px}
.tile-cap strong{display:block;font-size:17px;font-weight:400}
.tile-cap span{font-size:10px}
.tile-cap.right{text-align:right}
.tile-btn{position:absolute;left:50%;top:50%;transform:translate(-50%,-50%);background:var(--blue);color:#fff;font-size:12px;padding:4px 14px;border:1px solid #fff}

.news{height:232px;background:var(--grey);border-top:1px solid var(--line);display:flex;justify-content:center;gap:20px;padding-top:14px}
.news-col{width:226px}
.news-date{font-size:10px;color:var(--muted);border-bottom:1px solid #ccc;padding-bottom:5px;margin-bottom:10px}
.news-col h4{font-size:19px;font-weight:400;line-height:1.1;margin-bottom:8px}
.news-col p{font-size:10px;line-height:1.4;color:#555}
.read-more{display:flex;align-items:center;gap:5px;font-size:10px;color:var(--blue);margin-top:10px}
.read-more i{width:12px;height:12px;border-radius:50%;background:var(--blue);display:inline-block}
.news-links li{list-style:none;font-size:12px;line-height:1.3;color:var(--blue);margin-bottom:12px}

.contact{height:270px;display:flex;justify-content:center;gap:40px;padding-top:40px}
.reach,.form{width:340px}
.contact h3{font-size:20px;font-weight:400;color:#444;border-bottom:1px solid var(--line);padding-bottom:5px;margin-bottom:14px}
.reach-row{display:flex;gap:10px;align-items:flex-start;font-size:11px;color:#555;margin-bottom:14px}
.reach-row i{width:16px;height:16px;border-radius:50%;background:#aaa;flex:none}
.form-grid{display:grid;grid-template-columns:1fr 1fr;gap:6px 10px;font-size:10px;color:#555}
.field{border:1px solid #ccc;height:18px;padding:2px 4px}
.field.msg{grid-column:1/3;height:40px}
.submit{margin-top:8px;display:inline-block;border:1px solid #ccc;font-size:10px;padding:2px 10px;color:#555}

.site-footer{position:absolute;left:0;top:1940px;width:1200px;height:276px;background:var(--green);color:#fff}
.foot-cols{display:flex;justify-content:center;gap:40px;padding-top:30px}
.foot-col{width:150px}
.foot-col h5{font-size:11px;font-weight:700;margin-bottom:6px;text-transform:uppercase}
.foot-col li{list-style:none;font-size:10px;line-height:1.55}
.socials{display:flex;justify-content:center;gap:10px;margin-top:36px}
.socials span{width:24px;height:24px;border-radius:50%;border:2px solid #fff;display:block}
.copyright{position:absolute;bottom:0;left:0;right:0;height:36px;background:var(--green-dark);font-size:11px;display:flex;align-items:center;justify-content:center}
</style>
</head>
<body>
<header class="site-header">
  <div class="brand"><span class="brand-dot"></span>Brightfall Systems</div>
  <nav class="main-nav">
    <a class="active" href="#">Home</a><a href="#">Company</a><a href="#">Services</a><a href="#">Product</a><a href="#">Technology</a><a href="#">Communications</a><a href="#">Contact Us</a>
  </nav>
</header>

<section class="hero">
  <div class="hero-photo" role="img" aria-label="Dark home theater room with rows of seats facing a large screen"></div>
  <div class="hero-box">
    <div class="hero-title">Brightfall Systems</div>
    <div class="hero-tag">Where sound and light come together</div>
    <p class="hero-text">Lorem Ipsum is simply dummy text of the printing and typesetting industry. Lorem Ipsum has been the industry's standard dummy text ever since the 1500s, when an unknown printer took a galley of type and scrambled it to make a type specimen book. It has survived not only five centuries.</p>
  </div>
  <div class="hero-btn">Click to Read More</div>
  <div class="hero-arrow prev"><svg width="12" height="12" viewBox="0 0 12 12"><path d="M8 1L3 6l5 5" stroke="#333" stroke-width="2" fill="none"/></svg></div>
  <div class="hero-arrow next"><svg width="12" height="12" viewBox="0 0 12 12"><path d="M4 1l5 5-5 5" stroke="#333" stroke-width="2" fill="none"/></svg></div>
</section>

<section class="actions">
  <div class="action">
    <svg width="40" height="40" viewBox="0 0 40 40"><circle cx="20" cy="12" r="8" fill="#fff"/><path d="M5 38c0-10 6-16 15-16s15 6 15 16z" fill="#fff"/></svg>
    <h3>Demo Request</h3><p>To get our services</p><span class="btn-go">Go</span>
  </div>
  <div class="action">
    <svg width="44" height="40" viewBox="0 0 44 40"><rect x="3" y="3" width="38" height="26" rx="2" fill="none" stroke="#fff" stroke-width="3"/><rect x="18" y="29" width="8" height="6" fill="#fff"/><rect x="12" y="35" width="20" height="3" fill="#fff"/></svg>
    <h3>Signup</h3><p>As a new Customer</p><span class="btn-go">Go</span>
  </div>
  <div class="action">
    <svg width="44" height="40" viewBox="0 0 44 40"><rect x="2" y="4" width="26" height="20" fill="none" stroke="#fff" stroke-width="3"/><circle cx="32" cy="24" r="10" fill="none" stroke="#fff" stroke-width="3"/><path d="M22 24h20M32 14v20" stroke="#fff" stroke-width="2"/><rect x="8" y="28" width="14" height="3" fill="#fff"/></svg>
    <h3>News &amp; Updates</h3><p>Get to know more about us</p><span class="btn-go">Go</span>
  </div>
</section>

<section class="welcome">
  <h1>Welcome to Brightfall Systems</h1>
  <p>Lorem Ipsum is simply dummy text of the printing and typesetting industry. Lorem Ipsum has been the industry's standard dummy text ever since the 1500s, when an unknown printer took a galley of type and scrambled it to make a type specimen book. It has survived not only five centuries, but also the leap into electronic typesetting, remaining essentially unchanged.</p>
  <span class="btn-outline">Read More</span>
</section>

<section class="why">
  <h2>Why Brightfall?</h2>
  <div class="why-grid">
    <div class="tile"><div class="photo" role="img" aria-label="Hands reviewing charts and system plans on a desk" style="background:linear-gradient(135deg,#dfe8ef,#9fb6c8)"></div>
      <div class="tile-cap"><strong>System Design</strong><span>Lorem Ipsum is simply dummy text of the printing</span></div></div>
    <div class="tile"><div class="photo" role="img" aria-label="Warm lit living room with a home theater setup" style="background:linear-gradient(135deg,#c79a6a,#6e4a2e)"></div>
      <div class="tile-cap right"><strong>Home Theaters</strong><span>Lorem Ipsum is simply dummy text of the printing</span></div></div>
    <div class="tile"><div class="photo" role="img" aria-label="Green circuit board and network connections" style="background:linear-gradient(135deg,#7fb86a,#2f6e3a)"></div>
      <div class="tile-btn">Read More</div></div>
    <div class="tile"><div class="photo" role="img" aria-label="Conference room table with a presentation screen" style="background:linear-gradient(135deg,#8fa4b8,#3d4e60)"></div>
      <div class="tile-cap right"><strong>Conference Rooms</strong><span>Lorem Ipsum is simply dummy text of the printing</span></div></div>
  </div>
</section>

<section class="news">
  <div class="news-col">
    <div class="news-date">28 Feb 2017</div>
    <h4>Lorem Ipsum is simply dummy text</h4>
    <p>There are many variations of passages of Lorem Ipsum available, but the majority have suffered alteration in some form, by injected humour, or randomised words which don't look even slightly believable.</p>
    <div class="read-more"><i></i>Read more</div>
  </div>
  <div class="news-col">
    <div class="news-date">28 Feb 2017</div>
    <h4>Lorem Ipsum is simply dummy text</h4>
    <p>There are many variations of passages of Lorem Ipsum available, but the majority have suffered alteration in some form, by injected humour, or randomised words which don't look even slightly believable.</p>
    <div class="read-more"><i></i>Read more</div>
  </div>
  <div class="news-col">
    <div class="news-date">28 Feb 2017</div>
    <ul class="news-links">
      <li>Lorem Ipsum is simply dummy text</li>
      <li>It has survived not only five centuries, but also the leap</li>
      <li>It is a long established fact that a reader will be distracted</li>
      <li>Contrary to popular belief</li>
    </ul>
  </div>
</section>

<section class="contact">
  <div class="reach">
    <h3>Reach Us</h3>
    <div class="reach-row"><i></i><span>1400 Lakeview Drive Suite 120,<br>Marlow Ridge, ST 48213</span></div>
    <div class="reach-row"><i></i><span>info@brightfallsys.com</span></div>
    <div class="reach-row"><i></i><span>(540) 555-0148</span></div>
  </div>
  <div class="form">
    <h3>Contact Us</h3>
    <div class="form-grid">
      <div>Name</div><div>Subject</div>
      <div class="field"></div><div class="field"></div>
      <div>Phone #</div><div>Email</div>
      <div class="field"></div><div class="field"></div>
      <div class="field msg"></div>
    </div>
    <span class="submit">Submit</span>
  </div>
</section>

<footer class="site-footer">
  <div class="foot-cols">
    <div class="foot-col"><h5>Company</h5><ul><li>About Us</li><li>Management</li><li>Mission Statement</li><li>Philosophy</li><li>Customer Commitment</li></ul></div>
    <div class="foot-col"><h5>Services</h5><ul><li>System Design</li><li>Installation</li><li>Programming</li><li>Service &amp; Support</li><li>Maintenance</li><li>Consulting</li></ul></div>
    <div class="foot-col"><h5>Technology</h5><ul><li>Home Theater</li><li>Distributed Audio</li><li>Lighting Control</li><li>Building Automation</li><li>Security Cameras</li><li>Projectors</li></ul></div>
    <div class="foot-col"><h5>Communications</h5><ul><li>Video Conferencing</li><li>Conference Rooms</li><li>Networks</li><li>Phone Systems</li></ul></div>
  </div>
  <div class="socials"><span></span><span></span><span></span></div>
  <div class="copyright">© 2015 Brightfall Systems | All Rights Reserved</div>
</footer>
</body>
</html>
```